BIX Promotional flyer for students

We're looking for an 8.5" x 11" flyer that will be distributed to schools. Please see language to include in attached files.

Target Market(s)

The parents and teachers of high school students

Industry/Entity Type

Mental health

Other font styles liked:
• Monserrat and Roboto Slab

Requirements
Must have
• See attached pdf for language to be included on the flyer. Please use the color palette from our website: www.bixzone.tv. Please include some imagery of students. Please ensure the
Nice to have
• Feel free to use any of the graphics provided. See our website for our brand look & feel: www.bixzone.tv

```html
<!DOCTYPE html>
<html lang="en">
<head>
<meta charset="UTF-8">
<title>BIX – Fundraise Flyer</title>
<link rel="stylesheet" href="https://fonts.googleapis.com/css2?family=Quicksand:wght@500;600;700&family=Montserrat:wght@500;600&display=swap">
<style>
  :root {
    --orange: #ee7a1e;
    --orange-deep: #e8601a;
    --orange-light: #f58a2a;
    --charcoal: #333333;
    --ink: #1f1f1f;
    --white: #ffffff;
    --rule: #9a9a9a;
  }
  * { margin: 0; padding: 0; box-sizing: border-box; }
  html, body { width: 900px; height: 1200px; overflow: hidden; background: var(--white); }
  .flyer {
    position: relative;
    width: 900px;
    height: 1200px;
    overflow: hidden;
    background: var(--white);
    font-family: "Quicksand", "Montserrat", sans-serif;
  }
  .backdrop {
    position: absolute;
    left: 0; top: 300px;
    width: 900px; height: 900px;
    background: linear-gradient(180deg, rgba(210,210,210,0) 0%, #dcdcdc 35%, #e6e6e6 60%, #f6f6f6 85%, var(--white) 100%);
  }
  .art { position: absolute; left: 0; top: 0; }
  .brand {
    position: absolute;
    left: 34px; top: 36px;
    display: flex; align-items: center; gap: 14px;
  }
  .brand-dot {
    width: 52px; height: 52px;
    border-radius: 50%;
    background: var(--orange);
  }
  .brand-name {
    font-size: 60px;
    font-weight: 700;
    line-height: 1;
    color: var(--charcoal);
  }
  .headline {
    position: absolute;
    left: 0; width: 900px; top: 800px;
    text-align: center;
    font-size: 62px;
    font-weight: 700;
    color: var(--charcoal);
    letter-spacing: -0.5px;
  }
  .headline .accent { color: var(--orange); }
  .subline {
    position: absolute;
    left: 0; width: 900px; top: 887px;
    text-align: center;
    font-size: 28px;
    font-weight: 700;
    color: var(--ink);
  }
  .subline .divider {
    display: inline-block;
    width: 2px; height: 30px;
    background: var(--orange);
    vertical-align: -6px;
    margin: 0 14px;
  }
  .cta {
    position: absolute;
    left: 215px; top: 934px;
    width: 485px; height: 48px;
    border-radius: 24px;
    background: var(--orange);
    color: var(--white);
    font-size: 26px;
    font-weight: 600;
    text-align: center;
    line-height: 48px;
  }
  .blurb {
    position: absolute;
    left: 80px; width: 760px; top: 1002px;
    text-align: center;
    font-size: 17px;
    font-weight: 600;
    line-height: 1.3;
    color: var(--ink);
  }
  .rule {
    position: absolute;
    left: 310px; width: 300px; height: 3px;
    background: linear-gradient(90deg, transparent, var(--rule) 30%, var(--rule) 70%, transparent);
  }
  .rule.top { top: 1092px; }
  .rule.bottom { top: 1156px; }
  .site {
    position: absolute;
    left: 0; width: 900px; top: 1110px;
    text-align: center;
    font-family: "Montserrat", sans-serif;
    font-size: 18px;
    font-weight: 600;
    letter-spacing: 4px;
    color: var(--ink);
  }
</style>
</head>
<body>
<main class="flyer">
  <div class="backdrop" role="img" aria-label="Soft grey faded photo of a school outdoor scene"></div>

  <svg class="art" width="900" height="1200" viewBox="0 0 900 1200">
    <defs>
      <linearGradient id="photo-tone" x1="0" y1="0" x2="1" y2="1">
        <stop offset="0" stop-color="#d8d2cb"/>
        <stop offset="0.5" stop-color="#8d8a86"/>
        <stop offset="1" stop-color="#e4e4e2"/>
      </linearGradient>
      <clipPath id="accent-clip">
        <circle cx="765" cy="300" r="480"/>
      </clipPath>
    </defs>
    <g class="accent-field">
      <circle cx="745" cy="310" r="505" fill="var(--charcoal)"/>
      <circle cx="765" cy="300" r="480" fill="var(--orange-deep)"/>
      <g clip-path="url(#accent-clip)">
        <circle cx="860" cy="120" r="220" fill="#d9661c" opacity="0.55"/>
        <circle cx="880" cy="560" r="230" fill="var(--orange-light)" opacity="0.55"/>
        <circle cx="830" cy="780" r="170" fill="#f06a1c" opacity="0.6"/>
      </g>
    </g>
    <g class="portrait-frame">
      <circle cx="462" cy="442" r="345" fill="var(--charcoal)"/>
      <circle cx="472" cy="432" r="326" fill="var(--white)"/>
      <circle cx="472" cy="432" r="310" fill="url(#photo-tone)" role="img" aria-label="Photo of a young woman holding a mug, looking out of a window"/>
    </g>
  </svg>

  <div class="brand">
    <span class="brand-dot"></span>
    <span class="brand-name">BIX</span>
  </div>

  <h1 class="headline"><span class="accent">Fundraise</span> with BIX</h1>
  <p class="subline">50% of all proceeds<span class="divider"></span>Go back to your school</p>
  <div class="cta">Support the mental health</div>
  <p class="blurb">BIX is a simple and effective way to improve mental health. Your students will learn valuable coping skills and techniques from expert clinicians who analyze real cases and share their insights and advice.</p>
  <div class="rule top"></div>
  <p class="site">WWW.BIXZONE.TV</p>
  <div class="rule bottom"></div>
</main>
</body>
</html>
```